New iOS App design for Boston Startup

We are looking for a new app design for our Zorvak app. The current app's design feels outdated and we like to add lots of new functionality and a new navigation as well. A complete overhaul therefore!
We want you to design 5 screens that will have changed the most. The complete wireframes of these 5 pages are attached in the requirements document.
Once the winning design is selected we will award the winner with the designing all other screens (40-50 screens based on the same design). This will be a separate project worth $1000. The winning designer can get more follow up work if both sides are happy about the cooperation.
We will give feedback as soon as the first screen has been uploaded for review. Final decision will be made only after all 5 screens are finished.
We hope you give it your best!
Note: will only communicate through PixelGuild (no skype),
Updates
Project Deadline Extended
Reason: Want to give designers a chance to submit their designs as I understand from some, the deadline is too close.
I have raised the award and introduced a 2nd price as well to make it worth your time. I hope you give it your best shot.
Project Deadline Extended
Reason: A few of you have asked for an extension of the deadline as time is running out. I will extend by one day. Tell me if you need more.
Industry/Entity Type
Startup
Requirements
Must have
- At least 1 screen before we can give you feedback.
Nice to have
- multiple options of 1 screen to get to a desirable design

```html
<!DOCTYPE html>
<html lang="en">
<head>
<meta charset="utf-8">
<title>Home screen options</title>
<link rel="stylesheet" href="https://fonts.googleapis.com/css2?family=Lato:wght@300;400;700&display=swap">
<style>
  :root{
    --brand:#1bafd6;
    --brand-dark:#1597bb;
    --paper:#e7f2f9;
    --card:#ffffff;
    --ink:#6a6a6a;
    --ink-soft:#8a8a8a;
    --rule:#c9d3d9;
    --up:#2ccb55;
    --down:#ef4a4a;
    --stage-top:#b4b9b9;
    --stage-bottom:#9ea4b1;
  }
  *{box-sizing:border-box;margin:0;padding:0}
  html,body{width:1200px;height:1000px;overflow:hidden}
  body{
    background:linear-gradient(180deg,var(--stage-top),var(--stage-bottom));
    font-family:"Lato",sans-serif;
    position:relative;
  }
  .screen{
    position:absolute;width:380px;height:564px;
    background:var(--paper);
    box-shadow:0 8px 22px rgba(0,0,0,.22);
    display:flex;flex-direction:column;overflow:hidden;
  }
  .screen--a{left:20px;top:228px}
  .screen--b{left:410px;top:193px}
  .screen--c{left:800px;top:160px}

  .topbar{height:62px;flex:none;background:var(--brand);position:relative;display:flex;align-items:center;justify-content:center}
  .topbar__menu{position:absolute;left:22px;top:20px}
  .topbar__title{font-weight:300;font-size:32px;color:#fff;letter-spacing:-.5px}

  .content{flex:1;padding:0 12px;display:flex;flex-direction:column;align-items:center}
  .welcome{width:100%;height:62px;background:var(--card);margin-top:2px;text-align:center;color:var(--brand);padding-top:8px}
  .welcome__greet{font-size:15px;line-height:16px}
  .welcome__name{font-size:34px;font-weight:400;line-height:36px}

  .score{text-align:center;margin-top:5px}
  .score__label{font-size:10px;color:var(--ink);letter-spacing:.3px}
  .score__row{display:flex;align-items:center;justify-content:center;gap:6px;color:var(--ink)}
  .score__value{font-size:38px;font-weight:400;line-height:40px}
  .score__delta{font-size:24px;margin-left:6px;margin-top:6px}

  .period{font-size:17px;color:var(--brand);margin-top:4px}

  .stats{width:100%;display:flex;align-items:center;height:50px;margin-top:6px}
  .stats__track{flex:1;display:flex;overflow:hidden;height:100%;align-items:center}
  .stat{flex:0 0 118px;text-align:center}
  .stat__label{font-size:15px;color:var(--brand);line-height:18px}
  .stat__value{font-size:19px;font-weight:700;color:var(--ink);display:flex;align-items:center;justify-content:center;gap:2px;line-height:24px}
  .stat--period{flex:0 0 70px;font-size:19px;color:var(--brand);text-align:left}
  .chev{flex:none;width:20px;display:flex;justify-content:center}

  .rule{width:100%;height:1px;background:var(--rule);margin-top:8px}

  .shortcuts{width:356px;height:62px;background:var(--card);margin-top:14px;box-shadow:0 2px 4px rgba(0,0,0,.18);display:flex;align-items:flex-end;padding-bottom:6px}
  .shortcut{flex:1;display:flex;flex-direction:column;align-items:center;font-size:12px;color:var(--ink)}
  .shortcut--active{color:var(--brand)}
  .shortcut__count{font-size:25px;color:var(--brand);line-height:28px}

  .upnext{font-size:19px;color:var(--ink);margin-top:34px}
  .lesson{width:100%;height:44px;background:var(--brand);color:#fff;font-size:19px;display:flex;align-items:center;justify-content:center;margin-top:12px}

  .screen--c .stats{margin-top:2px}
  .screen--c .upnext{margin-top:48px}

  .tabbar{height:62px;flex:none;background:#fafafa;display:flex;border-top:1px solid #dcdcdc}
  .tab{flex:1;display:flex;flex-direction:column;align-items:center;justify-content:flex-end;padding-bottom:6px;font-size:10px;color:var(--ink-soft);gap:3px;position:relative}
  .tab--active{color:var(--brand)}
  .tab--active::before{content:"";position:absolute;top:-1px;left:0;right:0;height:3px;background:var(--brand)}
</style>
</head>
<body>

<!-- shared icon symbols -->
<svg width="0" height="0" style="position:absolute">
  <defs>
    <symbol id="i-menu" viewBox="0 0 24 20"><rect y="0" width="24" height="3.5" fill="#fff"/><rect y="8" width="24" height="3.5" fill="#fff"/><rect y="16" width="24" height="3.5" fill="#fff"/></symbol>
    <symbol id="i-left" viewBox="0 0 12 20"><path d="M10 2 L3 10 L10 18" stroke="#1bafd6" stroke-width="3.5" fill="none"/></symbol>
    <symbol id="i-right" viewBox="0 0 12 20"><path d="M2 2 L9 10 L2 18" stroke="#1bafd6" stroke-width="3.5" fill="none"/></symbol>
    <symbol id="i-up" viewBox="0 0 10 14"><path d="M5 0 L10 6 H6.5 V14 H3.5 V6 H0 Z" fill="#2ccb55"/></symbol>
    <symbol id="i-down" viewBox="0 0 16 22"><path d="M5 0 H11 V11 H16 L8 22 L0 11 H5 Z" fill="#ef4a4a"/></symbol>
    <symbol id="i-bars" viewBox="0 0 36 28"><rect x="2" y="12" width="8" height="14" fill="#1bafd6"/><rect x="12" y="2" width="8" height="24" fill="#1bafd6"/><rect x="22" y="9" width="8" height="17" fill="#1bafd6"/><rect x="0" y="26" width="36" height="2" fill="#1bafd6"/></symbol>
    <symbol id="i-doc" viewBox="0 0 32 32"><path d="M4 1 H20 L26 7 V31 H4 Z" fill="none" stroke="#777" stroke-width="1.5"/><path d="M8 10 H18 M8 14 H16 M8 18 H14 M8 22 H14" stroke="#777" stroke-width="1.2"/><circle cx="22" cy="18" r="5" fill="#fff" stroke="#777" stroke-width="1.5"/><path d="M25.5 21.5 L30 27" stroke="#777" stroke-width="2"/></symbol>
    <symbol id="i-book" viewBox="0 0 36 26"><path d="M2 3 Q10 0 18 4 Q26 0 34 3 V24 Q26 21 18 25 Q10 21 2 24 Z M18 4 V25" fill="none" stroke="#888" stroke-width="1.6"/></symbol>
    <symbol id="i-grid" viewBox="0 0 30 30"><rect x="1" y="1" width="28" height="28" fill="none" stroke="#888" stroke-width="1.5"/><path d="M15 1 V29 M1 15 H29" stroke="#888" stroke-width="1.5"/><text x="8" y="12" font-size="10" text-anchor="middle" fill="#777" font-family="Lato,sans-serif">a</text><text x="22" y="12" font-size="10" text-anchor="middle" fill="#777" font-family="Lato,sans-serif">b</text><text x="8" y="26" font-size="10" text-anchor="middle" fill="#777" font-family="Lato,sans-serif">c</text><text x="22" y="26" font-size="10" text-anchor="middle" fill="#777" font-family="Lato,sans-serif">d</text></symbol>
    <symbol id="i-home" viewBox="0 0 40 34"><path d="M20 1 L39 17 H34 V33 H24 V23 H16 V33 H6 V17 H1 Z" fill="#1bafd6"/></symbol>
    <symbol id="i-pad" viewBox="0 0 40 26"><path d="M9 3 H31 Q38 3 39 14 Q40 24 34 24 Q30 24 27 18 H13 Q10 24 6 24 Q0 24 1 14 Q2 3 9 3 Z" fill="none" stroke="#888" stroke-width="1.6"/><path d="M10 9 V15 M7 12 H13" stroke="#888" stroke-width="1.6"/><circle cx="28" cy="10" r="1.6" fill="#888"/><circle cx="31" cy="13" r="1.6" fill="#888"/></symbol>
    <symbol id="i-test" viewBox="0 0 30 32"><path d="M2 4 H22 V31 H2 Z" fill="none" stroke="#888" stroke-width="1.5"/><path d="M6 12 H16 M6 17 H16 M6 22 H14" stroke="#888" stroke-width="1.2"/><path d="M26 1 L29 4 L16 17 L12 18 L13 14 Z" fill="#fff" stroke="#888" stroke-width="1.5"/></symbol>
  </defs>
</svg>

<!-- Option A: period label above the stats -->
<section class="screen screen--a">
  <header class="topbar">
    <svg class="topbar__menu" width="24" height="20"><use href="#i-menu"/></svg>
    <h1 class="topbar__title">Home</h1>
  </header>
  <main class="content">
    <div class="welcome"><p class="welcome__greet">Welcome back,</p><p class="welcome__name">TAMIR</p></div>
    <div class="score">
      <p class="score__label">SCORE</p>
      <div class="score__row"><span class="score__value">650</span><svg width="16" height="22"><use href="#i-down"/></svg><span class="score__delta">-18</span></div>
    </div>
    <p class="period">Today</p>
    <div class="stats" style="margin-top:0">
      <span class="chev"><svg width="12" height="20"><use href="#i-left"/></svg></span>
      <div class="stats__track">
        <div class="stat"><p class="stat__label">Completion</p><p class="stat__value">34%<svg width="10" height="14"><use href="#i-up"/></svg>+4</p></div>
        <div class="stat"><p class="stat__label">Sessions</p><p class="stat__value">20<svg width="10" height="14"><use href="#i-up"/></svg>+3</p></div>
        <div class="stat"><p class="stat__label">Min.</p><p class="stat__value">18<svg width="10" height="14"><use href="#i-up"/></svg>+10</p></div>
      </div>
      <span class="chev"><svg width="12" height="20"><use href="#i-right"/></svg></span>
    </div>
    <div class="rule"></div>
    <nav class="shortcuts">
      <div class="shortcut shortcut--active"><svg width="36" height="28"><use href="#i-bars"/></svg>Analytics</div>
      <div class="shortcut"><svg width="32" height="32"><use href="#i-doc"/></svg>Course Overview</div>
      <div class="shortcut"><span class="shortcut__count">33</span>Days until test</div>
    </nav>
    <p class="upnext">Up Next:</p>
    <div class="lesson">Lesson 4 - Sentence Correction</div>
  </main>
  <nav class="tabbar">
    <div class="tab"><svg width="36" height="26"><use href="#i-book"/></svg>Theory</div>
    <div class="tab"><svg width="30" height="30"><use href="#i-grid"/></svg>Practice</div>
    <div class="tab tab--active"><svg width="40" height="34"><use href="#i-home"/></svg>Home</div>
    <div class="tab"><svg width="40" height="26"><use href="#i-pad"/></svg>Games</div>
    <div class="tab"><svg width="30" height="32"><use href="#i-test"/></svg>Tests</div>
  </nav>
</section>

<!-- Option B: weekly period -->
<section class="screen screen--b">
  <header class="topbar">
    <svg class="topbar__menu" width="24" height="20"><use href="#i-menu"/></svg>
    <h1 class="topbar__title">Home</h1>
  </header>
  <main class="content">
    <div class="welcome"><p class="welcome__greet">Welcome back,</p><p class="welcome__name">TAMIR</p></div>
    <div class="score">
      <p class="score__label">SCORE</p>
      <div class="score__row"><span class="score__value">650</span><svg width="16" height="22"><use href="#i-down"/></svg><span class="score__delta">-18</span></div>
    </div>
    <p class="period">This Week</p>
    <div class="stats" style="margin-top:0">
      <span class="chev"><svg width="12" height="20"><use href="#i-left"/></svg></span>
      <div class="stats__track">
        <div class="stat"><p class="stat__label">Completion</p><p class="stat__value">34%<svg width="10" height="14"><use href="#i-up"/></svg>+4</p></div>
        <div class="stat"><p class="stat__label">Sessions</p><p class="stat__value">20<svg width="10" height="14"><use href="#i-up"/></svg>+3</p></div>
        <div class="stat"><p class="stat__label">Min.</p><p class="stat__value">18<svg width="10" height="14"><use href="#i-up"/></svg>+10</p></div>
      </div>
      <span class="chev"><svg width="12" height="20"><use href="#i-right"/></svg></span>
    </div>
    <div class="rule"></div>
    <nav class="shortcuts">
      <div class="shortcut shortcut--active"><svg width="36" height="28"><use href="#i-bars"/></svg>Analytics</div>
      <div class="shortcut"><svg width="32" height="32"><use href="#i-doc"/></svg>Course Overview</div>
      <div class="shortcut"><span class="shortcut__count">33</span>Days until test</div>
    </nav>
    <p class="upnext">Up Next:</p>
    <div class="lesson">Lesson 4 - Sentence Correction</div>
  </main>
  <nav class="tabbar">
    <div class="tab"><svg width="36" height="26"><use href="#i-book"/></svg>Theory</div>
    <div class="tab"><svg width="30" height="30"><use href="#i-grid"/></svg>Practice</div>
    <div class="tab tab--active"><svg width="40" height="34"><use href="#i-home"/></svg>Home</div>
    <div class="tab"><svg width="40" height="26"><use href="#i-pad"/></svg>Games</div>
    <div class="tab"><svg width="30" height="32"><use href="#i-test"/></svg>Tests</div>
  </nav>
</section>

<!-- Option C: period inline with the stats -->
<section class="screen screen--c">
  <header class="topbar">
    <svg class="topbar__menu" width="24" height="20"><use href="#i-menu"/></svg>
    <h1 class="topbar__title">Home</h1>
  </header>
  <main class="content">
    <div class="welcome"><p class="welcome__greet">Welcome back,</p><p class="welcome__name">TAMIR</p></div>
    <div class="score">
      <p class="score__label">SCORE</p>
      <div class="score__row"><span class="score__value">650</span><svg width="16" height="22"><use href="#i-down"/></svg><span class="score__delta">-18</span></div>
    </div>
    <div class="stats">
      <span class="chev"><svg width="12" height="20"><use href="#i-left"/></svg></span>
      <div class="stats__track">
        <div class="stat stat--period">Today</div>
        <div class="stat"><p class="stat__label">Completion</p><p class="stat__value">34%<svg width="10" height="14"><use href="#i-up"/></svg>+4</p></div>
        <div class="stat"><p class="stat__label">Sessions</p><p class="stat__value">20<svg width="10" height="14"><use href="#i-up"/></svg>+3</p></div>
        <div class="stat"><p class="stat__label">Min.</p><p class="stat__value">18<svg width="10" height="14"><use href="#i-up"/></svg>+10</p></div>
      </div>
      <span class="chev"><svg width="12" height="20"><use href="#i-right"/></svg></span>
    </div>
    <div class="rule"></div>
    <nav class="shortcuts">
      <div class="shortcut shortcut--active"><svg width="36" height="28"><use href="#i-bars"/></svg>Analytics</div>
      <div class="shortcut"><svg width="32" height="32"><use href="#i-doc"/></svg>Course Overview</div>
      <div class="shortcut"><span class="shortcut__count">33</span>Days until test</div>
    </nav>
    <p class="upnext">Up Next:</p>
    <div class="lesson">Lesson 4 - Sentence Correction</div>
  </main>
  <nav class="tabbar">
    <div class="tab"><svg width="36" height="26"><use href="#i-book"/></svg>Theory</div>
    <div class="tab"><svg width="30" height="30"><use href="#i-grid"/></svg>Practice</div>
    <div class="tab tab--active"><svg width="40" height="34"><use href="#i-home"/></svg>Home</div>
    <div class="tab"><svg width="40" height="26"><use href="#i-pad"/></svg>Games</div>
    <div class="tab"><svg width="30" height="32"><use href="#i-test"/></svg>Tests</div>
  </nav>
</section>

</body>
</html>
```